Dusty Trail Outfitters Home Page

I need a logo and page design for my home page, maybe some background color suggestions to go with it. I want the logo to project "vintage" and "western wear" but not be your typical trite western saddle and gun type thing.
http://www.dustytrailoutfitters.example/store/cart.php
Not looking for page coding just logo and other design elements to lay in over the site's template to make it "pop"
Target Market(s)
My customers are 70/30 men to women.
Industry/Entity Type
Gun
Font styles to use

```html
<!DOCTYPE html>
<html lang="en">
<head>
<meta charset="utf-8">
<title>Dusty Trail Outfitters – Header Concepts</title>
<link href="https://fonts.googleapis.com/css2?family=Lato:wght@700;900&family=Kaushan+Script&display=swap" rel="stylesheet">
<style>
  :root {
    --canvas: #cdb999;
    --canvas-light: #d4c2a4;
    --teal: #3a97a9;
    --teal-dark: #2c7f90;
    --charcoal: #262626;
    --charcoal-light: #333231;
    --cream: #efe3c6;
    --pill: #e7dcc5;
    --ink: #2e2a25;
    --gold: #f2c45a;
    --sky: #4aa3bb;
    --mist: #6fb0c0;
  }
  * { margin: 0; padding: 0; box-sizing: border-box; }
  html, body { width: 1200px; height: 1000px; overflow: hidden; }
  body {
    position: relative;
    background:
      repeating-linear-gradient(45deg, rgba(255,255,255,0.05) 0 2px, transparent 2px 5px),
      repeating-linear-gradient(-45deg, rgba(0,0,0,0.03) 0 2px, transparent 2px 6px),
      linear-gradient(var(--canvas-light), var(--canvas));
    font-family: "Lato", Arial, sans-serif;
  }
  .header-concept {
    position: absolute;
    left: 0;
    width: 1200px;
    height: 166px;
    background: linear-gradient(var(--teal), var(--teal-dark) 50%, var(--teal));
    box-shadow: 0 3px 4px rgba(0,0,0,0.35);
  }
  .header-concept.one { top: 146px; }
  .header-concept.two { top: 417px; }
  .header-concept.three { top: 691px; }
  .grunge-band {
    position: absolute;
    left: 0; right: 0;
    top: 17px; height: 132px;
    background:
      radial-gradient(ellipse at 20% 40%, var(--charcoal-light), transparent 60%),
      radial-gradient(ellipse at 70% 60%, var(--charcoal-light), transparent 55%),
      var(--charcoal);
  }
  .brand {
    position: absolute;
    left: 60px; top: 0;
    width: 405px; height: 166px;
    display: flex;
    align-items: center;
    justify-content: center;
    gap: 14px;
  }
  .brand-dot {
    width: 26px; height: 26px;
    border-radius: 50%;
    flex: none;
  }
  .one .brand-dot { background: var(--gold); }
  .two .brand-dot { background: var(--sky); }
  .three .brand-dot { background: var(--mist); }
  .brand-name {
    font-family: "Lato", Arial, sans-serif;
    font-weight: 900;
    font-size: 34px;
    line-height: 1.05;
    color: var(--cream);
    letter-spacing: 1px;
  }
  .tagline {
    position: absolute;
    left: 476px; top: 87px;
    font-family: "Kaushan Script", cursive;
    font-size: 22px;
    color: var(--cream);
    white-space: nowrap;
  }
  .search {
    position: absolute;
    left: 901px; top: 52px;
    display: flex;
    align-items: center;
    gap: 10px;
  }
  .search-field {
    width: 173px; height: 30px;
    border-radius: 15px;
    background: var(--pill);
    color: var(--ink);
    font-weight: 700;
    font-size: 17px;
    line-height: 30px;
    padding-left: 17px;
  }
  .search-go {
    color: var(--cream);
    font-weight: 700;
    font-size: 18px;
  }
</style>
</head>
<body>
  <header class="header-concept one">
    <div class="grunge-band"></div>
    <div class="brand"><span class="brand-dot"></span><span class="brand-name">Dusty Trail<br>Outfitters</span></div>
    <p class="tagline">Brand-New Retro Styled Western Wear</p>
    <div class="search"><span class="search-field">Search...</span><span class="search-go">GO!</span></div>
  </header>

  <header class="header-concept two">
    <div class="grunge-band"></div>
    <div class="brand"><span class="brand-dot"></span><span class="brand-name">Dusty Trail<br>Outfitters</span></div>
    <p class="tagline">Brand-New Retro Styled Western Wear</p>
    <div class="search"><span class="search-field">Search...</span><span class="search-go">GO!</span></div>
  </header>

  <header class="header-concept three">
    <div class="grunge-band"></div>
    <div class="brand"><span class="brand-dot"></span><span class="brand-name">Dusty Trail<br>Outfitters</span></div>
    <p class="tagline">Brand-New Retro Styled Western Wear</p>
    <div class="search"><span class="search-field">Search...</span><span class="search-go">GO!</span></div>
  </header>
</body>
</html>
```